Fruit and Beverage importer and distributor. F&B industry. catering mainly to touristy venues/outlet

We need a stationary design for our company in Singapore called LurenPalm. We are a major importer and distributor of fresh thailand coconuts in Singapore hence the company name. but moving forward we intend to diversify into more fruits, juices, and beverage products to sell to our existing base of customers.
mainly catering to F&B outlets at hot tourist spots such as restaurants and theme parks and hotel chains. we core product is the fresh thai coconut. on the side we are distributing a couple of read to drink beverages
we would like to see designs that are fun and refreshing. think tropical holiday theme.
ive attached our company logo and a photo of a general look and feel id like to see for our stationary.
Industry/Entity Type
Catering
Look and feel
Each slider illustrates characteristics of the customer's brand and the style your logo design should communicate.

```html
<!DOCTYPE html>
<html lang="en">
<head>
<meta charset="utf-8">
<title>LurenPalm Business Card</title>
<link rel="stylesheet" href="https://fonts.googleapis.com/css2?family=Alfa+Slab+One&family=Roboto+Slab:wght@700&family=Noto+Sans+SC:wght@400;700&display=swap">
<style>
  :root {
    --backdrop: #d8d2ca;
    --sea: #7ccbdb;
    --sea-deep: #6bbccd;
    --cream: #f3ecd2;
    --cream-line: #e9dfbd;
    --coral: #e3202b;
    --white: #ffffff;
    --frond-light: #8fc43f;
    --frond-dark: #3f8a2a;
    --coconut: #7fb83a;
    --wave: #d8f1f6;
  }
  * { box-sizing: border-box; margin: 0; padding: 0; }
  html, body { width: 1200px; height: 900px; overflow: hidden; }
  body { background: var(--backdrop); position: relative; font-family: "Roboto Slab", serif; }

  .card {
    position: absolute;
    left: 270px;
    width: 660px;
    height: 377px;
    background: var(--cream);
    padding: 9px;
    box-shadow: 0 6px 18px rgba(0,0,0,0.18);
  }
  .card--front { top: 52px; }
  .card--back { top: 470px; }

  .card__face {
    position: relative;
    width: 100%;
    height: 100%;
    background: radial-gradient(ellipse at 50% 50%, var(--sea) 0%, var(--sea-deep) 100%);
    overflow: hidden;
  }
  .card__rule {
    position: absolute;
    inset: 6px;
    border: 2px solid var(--cream-line);
    pointer-events: none;
  }

  .frond {
    position: absolute;
    background: radial-gradient(ellipse at var(--origin), var(--frond-dark) 0%, var(--frond-light) 55%, rgba(143,196,63,0) 75%);
  }
  .frond--top-left { left: -40px; top: -30px; width: 260px; height: 180px; --origin: 15% 15%; }
  .frond--top-right { right: -40px; top: -30px; width: 260px; height: 170px; --origin: 85% 15%; }
  .frond--logo-tree { left: 380px; top: 16px; width: 90px; height: 80px; --origin: 50% 40%; }

  /* front */
  .brand {
    position: absolute;
    left: 0; right: 0;
    top: 130px;
    display: flex;
    align-items: center;
    justify-content: center;
    gap: 14px;
  }
  .brand__dot { width: 34px; height: 34px; border-radius: 50%; background: var(--coral); }
  .brand__name {
    font-family: "Alfa Slab One", serif;
    font-size: 58px;
    color: var(--coral);
    letter-spacing: 1px;
  }
  .company {
    position: absolute;
    left: 0; right: 0;
    top: 238px;
    text-align: center;
    color: var(--white);
  }
  .company__cn { font-family: "Noto Sans SC", sans-serif; font-size: 18px; letter-spacing: 2px; }
  .company__en { font-size: 15px; margin-top: 6px; letter-spacing: 0.5px; }

  /* back */
  .person {
    position: absolute;
    left: 0; right: 0;
    top: 48px;
    text-align: center;
    color: var(--coral);
  }
  .person__cn { font-family: "Noto Sans SC", sans-serif; font-weight: 700; font-size: 32px; line-height: 1.1; }
  .person__name {
    font-family: "Alfa Slab One", serif;
    font-size: 40px;
    line-height: 1.15;
    letter-spacing: 1px;
    -webkit-text-stroke: 1px var(--white);
    paint-order: stroke fill;
  }
  .person__title { font-family: "Alfa Slab One", serif; font-size: 21px; margin-top: 2px; letter-spacing: 0.5px; }

  .waves { position: absolute; left: 220px; top: 198px; }

  .contact, .address {
    position: absolute;
    top: 244px;
    color: var(--white);
    font-size: 17px;
    line-height: 1.4;
    letter-spacing: 0.5px;
  }
  .contact { left: 48px; }
  .address { left: 370px; top: 266px; }

  .drink {
    position: absolute;
    right: 40px;
    top: 170px;
    width: 100px;
    height: 110px;
    border-radius: 48% 48% 44% 44%;
    background: radial-gradient(circle at 45% 55%, var(--coconut) 0%, #a9d45a 70%, #f3d34a 100%);
  }
</style>
</head>
<body>

  <section class="card card--front">
    <div class="card__face">
      <div class="frond frond--top-left" role="img" aria-label="Palm fronds reaching in from the top left corner"></div>
      <div class="frond frond--top-right" role="img" aria-label="Palm fronds reaching in from the top right corner"></div>

      <div class="brand">
        <span class="brand__dot"></span>
        <span class="brand__name">LurenPalm</span>
      </div>

      <div class="company">
        <p class="company__cn">绿棕私人有限公司</p>
        <p class="company__en">Luren Palm Pte. Ltd.</p>
      </div>
      <div class="card__rule"></div>
    </div>
  </section>

  <section class="card card--back">
    <div class="card__face">
      <div class="frond frond--top-left" role="img" aria-label="Palm fronds reaching in from the top left corner"></div>
      <div class="frond frond--top-right" role="img" aria-label="Palm fronds reaching in from the top right corner"></div>

      <header class="person">
        <p class="person__cn">林志航</p>
        <h1 class="person__name">MARCUS HOLLEN</h1>
        <p class="person__title">Operation Manager</p>
      </header>

      <svg class="waves" width="200" height="40" viewBox="0 0 200 40" aria-hidden="true">
        <path d="M4 14 q16 -10 32 0 t32 0 t32 0 t32 0 t32 0 t32 0" fill="none" stroke="var(--wave)" stroke-width="2"/>
        <path d="M4 28 q16 -10 32 0 t32 0 t32 0 t32 0 t32 0 t32 0" fill="none" stroke="var(--wave)" stroke-width="2"/>
      </svg>

      <div class="contact">
        <p>(+65) 6 310 0482</p>
        <p>(+65) 6 2014 7731</p>
        <p>info@lurenpalm.com</p>
      </div>

      <div class="address">
        <p>Keppel 8-2, 09872</p>
        <p>Harbourton, Country</p>
        <p>lurenpalm.com</p>
      </div>

      <div class="drink" role="img" aria-label="Illustration of a fresh coconut drink with a straw, umbrella, fruit and a frangipani flower"></div>
      <div class="card__rule"></div>
    </div>
  </section>

</body>
</html>
```